TorvaLink.com

We need a new web design for our seo services website at torvalink.com.

Right now we have our homepage, and 2 other pages which we use a html code generator. We need a header and footer and a nice professional looking design to showcase our seo plans.

As for the logo we'll use our company torvagrid.com logo Torva and change Grid to Link and Systems to Search Engine Marketing.

We also like to display our brivopages widget and author alert sign up box.

```html
<!DOCTYPE html>
<html lang="en">
<head>
<meta charset="utf-8">
<title>TorvaLink – SEO Plans</title>
<link rel="stylesheet" href="https://fonts.googleapis.com/css2?family=Arimo:wght@400;700&display=swap">
<style>
:root{
  --navy:#0d3d84;
  --red:#d0121b;
  --gold:#fcc400;
  --plan-grey:#9d9d9d;
  --plan-top:#c9c9c9;
  --header-bg:#f4f4f4;
  --bar-bg:#e6e6e6;
  --audit-bg:#e1ecec;
  --report-bg:#f2f2f2;
  --footer-bg:#1a1a1a;
  --text:#444;
  --muted:#8a8a8a;
  --line:#e4e4e4;
  --white:#fff;
}
*{box-sizing:border-box;margin:0;padding:0}
html,body{width:1200px;height:1117px;overflow:hidden}
body{position:relative;background:var(--white);font-family:"Arimo",Arial,sans-serif;color:var(--text)}
.abs{position:absolute}
ul{list-style:none}

/* header */
.site-header{left:0;top:0;width:1200px;height:70px;background:var(--header-bg)}
.brand{left:308px;top:16px;color:var(--navy);font-weight:700;line-height:1}
.brand-name{font-size:28px;letter-spacing:-.5px}
.brand-sub{font-size:12px;margin-top:3px;padding-left:72px}
.main-nav{right:309px;top:44px;font-size:8px;color:var(--navy);letter-spacing:.3px;display:flex;gap:10px}
.main-nav .sep{color:#666}

.sub-bar{left:0;top:70px;width:1200px;height:28px;background:var(--bar-bg)}
.tagline{left:308px;top:79px;font-size:9px;color:var(--navy);white-space:nowrap}
.promo-link{left:627px;top:80px;font-size:7px;color:var(--red);white-space:nowrap}
.quote-btn{left:800px;top:76px;width:91px;height:19px;background:var(--navy);border-radius:4px;color:var(--white);font-size:6.5px;font-weight:700;text-align:center;line-height:19px;white-space:nowrap}

/* slider */
.slider-art{left:308px;top:123px;width:568px;height:196px;background:linear-gradient(90deg,#f1f1f1 0%,#fff 35%,#eef3f8 55%,#fafcfe 100%)}
.slider-arrow{top:183px;width:38px;height:61px;background:#ececec;color:#c4c4c4;font-size:26px;text-align:center;line-height:59px}
.slider-arrow.prev{left:269px}
.slider-arrow.next{left:892px}
.slider-dots{left:567px;top:299px;display:flex;gap:3px}
.slider-dots i{display:block;width:9px;height:9px;background:var(--navy)}
.slider-dots i.on{background:var(--red)}

/* pricing */
.plan{top:324px;width:145px;height:140px}
.plan-body{position:absolute;left:0;top:6px;width:100%;height:109px;background:var(--plan-grey)}
.plan.featured .plan-body{background:var(--gold)}
.plan-body::before{content:"";position:absolute;left:0;top:0;width:100%;height:34px;background:var(--plan-top)}
.plan.featured .plan-body::before{background:var(--gold)}
.plan-tab{position:absolute;left:6px;top:0}
.plan-name{position:absolute;left:0;top:8px;width:100%;text-align:center;color:var(--white);font-size:13px}
.plan-price{position:absolute;left:20px;top:46px;color:var(--white);font-size:37px;line-height:1;white-space:nowrap}
.plan-price small{font-size:9px}
.plan-kw{position:absolute;left:0;top:90px;width:100%;text-align:center;font-size:10px;color:#333}
.plan-btn{position:absolute;left:6px;top:116px;width:131px;height:23px;background:var(--navy);border-radius:0 0 4px 4px;color:var(--white);font-size:10px;line-height:23px;padding-left:14px;white-space:nowrap}
.plan-btn svg{position:absolute;right:12px;top:4px}

/* tables */
.band{left:0;width:1200px}
.band.audit{top:495px;height:202px;background:var(--audit-bg)}
.band.report{top:697px;height:192px;background:var(--report-bg)}
.section-title{left:308px;font-size:10px;font-weight:400;color:#444;letter-spacing:.2px}
.section-text{left:308px;font-size:7px;color:#666;line-height:9.5px;width:360px}
.plan-table{left:308px;width:583px;background:var(--white);border-collapse:collapse;font-size:7px}
.plan-table th,.plan-table td{width:25%;border-right:1px solid var(--line);border-bottom:1px solid var(--line);text-align:left;padding-left:12px;font-weight:400}
.plan-table th:last-child,.plan-table td:last-child{border-right:0}
.plan-table th{color:var(--navy);height:21px}
.plan-table td{color:var(--muted);height:22px}

/* promo strip */
.promo-art{left:308px;top:899px;width:178px;height:93px;background:linear-gradient(135deg,#f4f4f4,#e6e6e6)}
.ad-slot{left:498px;top:939px;font-size:9.5px;color:#222}
.divider{left:570px;top:903px;width:4px;height:86px;background:var(--red)}
.articles-title{left:600px;top:903px;font-size:10px;font-weight:400;color:#444}
.article{left:600px;font-size:6.5px;color:#333;line-height:8px}
.article span{display:block;color:#aaa}
.article-rule{left:600px;width:130px;height:1px;background:var(--line)}
.all-articles{left:600px;top:980px;font-size:6.5px;color:var(--navy)}
.signup-text{left:746px;top:902px;font-size:6.5px;color:var(--red);line-height:8px;width:150px}
.signup-input{left:746px;top:925px;width:145px;height:18px;border:1px solid #ddd;font-size:6px;color:#bbb;padding:5px}
.signup-btn{left:746px;top:950px;width:60px;height:16px;background:var(--navy);color:var(--white);font-size:7.5px;text-align:center;line-height:16px}

/* footer */
.site-footer{left:0;top:996px;width:1200px;height:121px;background:var(--footer-bg)}
.footer-head{top:1032px;font-size:9.5px;color:var(--white);letter-spacing:.3px}
.footer-rule{top:1048px;width:88px;height:1px;background:#444}
.footer-links{top:1053px;font-size:7px;font-weight:400;color:var(--white);line-height:9px}
.footer-links li{color:var(--white);font-weight:400}
.social{left:599px;top:1070px;display:flex;gap:5px}
.social i{display:block;width:19px;height:19px;border-radius:4px;background:#3d3d3d}
.footer-brand{right:309px;top:1030px;color:var(--white);font-weight:700;text-align:right;line-height:1}
.footer-brand .brand-name{font-size:19px}
.footer-brand .brand-sub{font-size:7px;padding:0;margin-top:2px}
.copyright{right:309px;top:1075px;font-size:6px;color:#ccc;text-align:right}
</style>
</head>
<body>

<header>
  <div class="abs site-header"></div>
  <div class="abs brand">
    <div class="brand-name">TorvaGrid</div>
    <div class="brand-sub">Systems</div>
  </div>
  <nav class="abs main-nav"><span>HOME</span><span class="sep">|</span><span>LOCAL MARKETING</span><span class="sep">|</span><span>COMPETITIVE SEO</span></nav>
  <div class="abs sub-bar"></div>
  <div class="abs tagline">TorvaLink Internet Marketing and Search Engine Optimization Services</div>
  <div class="abs promo-link">Live Rank Tracking, Reports &amp; Much More &nbsp;»</div>
  <div class="abs quote-btn">REQUEST A FREE QUOTE</div>
</header>

<section>
  <div class="abs slider-art" role="img" aria-label="Slide artwork: HTML tags, a pencil ticking SEO basics, and a magnifying glass over the word SEO surrounded by keywords, rank, links, pages and content"></div>
  <div class="abs slider-arrow prev">‹</div>
  <div class="abs slider-arrow next">›</div>
  <div class="abs slider-dots"><i class="on"></i><i></i><i></i><i></i></div>
</section>

<section>
  <div class="abs plan" style="left:308px">
    <div class="plan-body"></div>
    <svg class="plan-tab" width="133" height="30" viewBox="0 0 133 30"><path d="M0 0H133V18L125 29H8L0 18Z" fill="#0d3d84"/></svg>
    <div class="plan-name">SILVER</div>
    <div class="plan-price">$500<small>/mo</small></div>
    <div class="plan-kw">UP TO 10 KEYWORDS</div>
    <div class="plan-btn">GET FREE QUOTE<svg width="15" height="15" viewBox="0 0 15 15"><circle cx="7.5" cy="7.5" r="7.5" fill="#fff"/><path d="M4 7.5H10M7.5 5L10 7.5L7.5 10" stroke="#0d3d84" stroke-width="1.6" fill="none"/></svg></div>
  </div>
  <div class="abs plan featured" style="left:454px">
    <div class="plan-body"></div>
    <svg class="plan-tab" width="133" height="30" viewBox="0 0 133 30"><path d="M0 0H133V18L125 29H8L0 18Z" fill="#0d3d84"/></svg>
    <div class="plan-name">GOLD</div>
    <div class="plan-price">$750<small>/mo</small></div>
    <div class="plan-kw">UP TO 20 KEYWORDS</div>
    <div class="plan-btn">GET FREE QUOTE<svg width="15" height="15" viewBox="0 0 15 15"><circle cx="7.5" cy="7.5" r="7.5" fill="#fff"/><path d="M4 7.5H10M7.5 5L10 7.5L7.5 10" stroke="#0d3d84" stroke-width="1.6" fill="none"/></svg></div>
  </div>
  <div class="abs plan" style="left:600px">
    <div class="plan-body"></div>
    <svg class="plan-tab" width="133" height="30" viewBox="0 0 133 30"><path d="M0 0H133V18L125 29H8L0 18Z" fill="#0d3d84"/></svg>
    <div class="plan-name">PLATINUM</div>
    <div class="plan-price" style="left:14px">$1200<small>/mo</small></div>
    <div class="plan-kw">UP TO 30 KEYWORDS</div>
    <div class="plan-btn">GET FREE QUOTE<svg width="15" height="15" viewBox="0 0 15 15"><circle cx="7.5" cy="7.5" r="7.5" fill="#fff"/><path d="M4 7.5H10M7.5 5L10 7.5L7.5 10" stroke="#0d3d84" stroke-width="1.6" fill="none"/></svg></div>
  </div>
  <div class="abs plan" style="left:746px">
    <div class="plan-body"></div>
    <svg class="plan-tab" width="133" height="30" viewBox="0 0 133 30"><path d="M0 0H133V18L125 29H8L0 18Z" fill="#0d3d84"/></svg>
    <div class="plan-name">PLATINUM +</div>
    <div class="plan-price" style="left:14px">$1300<small>/mo</small></div>
    <div class="plan-kw">UP TO 40 KEYWORDS</div>
    <div class="plan-btn">GET FREE QUOTE<svg width="15" height="15" viewBox="0 0 15 15"><circle cx="7.5" cy="7.5" r="7.5" fill="#fff"/><path d="M4 7.5H10M7.5 5L10 7.5L7.5 10" stroke="#0d3d84" stroke-width="1.6" fill="none"/></svg></div>
  </div>
</section>

<section>
  <div class="abs band audit"></div>
  <h2 class="abs section-title" style="top:517px">WEBSITE AUDIT - MONTH 1 SETUP</h2>
  <p class="abs section-text" style="top:540px">Insightful audits that help you understand what work needs to be done and what the website can rank for.<br>Our comprehensive site audit maximizes the effects of our methodology.</p>
  <table class="abs plan-table" style="top:572px">
    <tr><th>10 Pages Optimized</th><th>20 Pages Optimized</th><th>30 Pages Optimized</th><th>40 Pages Optimized</th></tr>
    <tr><td>Website Audit</td><td>Website Audit</td><td>Website Audit</td><td>Website Audit</td></tr>
    <tr><td>Website Audit</td><td>Website Audit</td><td>Website Audit</td><td>Website Audit</td></tr>
    <tr><td>Website Audit</td><td>Website Audit</td><td>Website Audit</td><td>Website Audit</td></tr>
    <tr><td>Website Audit</td><td>Website Audit</td><td>Website Audit</td><td>Website Audit</td></tr>
  </table>

  <div class="abs band report"></div>
  <h2 class="abs section-title" style="top:719px">REPORTING AND STRATEGY - MONTHLY</h2>
  <p class="abs section-text" style="top:739px">Our live dashboard always has up to date traffic information and search results rankings. You can log in at any time, or get a comprehensive PDF report showing rankings and traffic.</p>
  <table class="abs plan-table" style="top:768px">
    <tr><th>10 Pages Optimized</th><th>20 Pages Optimized</th><th>30 Pages Optimized</th><th>40 Pages Optimized</th></tr>
    <tr><td>Website Audit</td><td>Website Audit</td><td>Website Audit</td><td>Website Audit</td></tr>
    <tr><td>Website Audit</td><td>Website Audit</td><td>Website Audit</td><td>Website Audit</td></tr>
    <tr><td>Website Audit</td><td>Website Audit</td><td>Website Audit</td><td>Website Audit</td></tr>
  </table>
</section>

<section>
  <div class="abs promo-art" role="img" aria-label="Promo artwork: We do blogs and websites – custom, unique and branded e-commerce integrated optimised sites, with a figure holding a megaphone"></div>
  <div class="abs ad-slot">Add HERE</div>
  <div class="abs divider"></div>
  <h3 class="abs articles-title">Articles</h3>
  <div class="abs article" style="top:922px">Different Kinds of Internet Marketing<span>View Summary</span></div>
  <div class="abs article-rule" style="top:942px"></div>
  <div class="abs article" style="top:951px">Seven Ways to Promote Your New Website<span>View Summary</span></div>
  <div class="abs article-rule" style="top:971px"></div>
  <div class="abs all-articles">+view all articles</div>
  <p class="abs signup-text">Sign up to receive email alerts of Dylan Reyes's latest articles from BrivoPages.com!</p>
  <div class="abs signup-input">email@example.com</div>
  <div class="abs signup-btn">SIGN UP</div>
</section>

<footer>
  <div class="abs site-footer"></div>
  <div class="abs footer-head" style="left:308px">LINKS</div>
  <div class="abs footer-rule" style="left:308px"></div>
  <ul class="abs footer-links" style="left:308px"><li>Lorem Ipsum</li><li>Lorem Ipsum</li><li>Lorem Ipsum</li><li>Lorem Ipsum</li><li>Lorem Ipsum</li></ul>
  <div class="abs footer-head" style="left:450px">OTHERS LINKS</div>
  <div class="abs footer-rule" style="left:450px"></div>
  <ul class="abs footer-links" style="left:452px"><li>Lorem Ipsum</li><li>Lorem Ipsum</li><li>Lorem Ipsum</li><li>Lorem Ipsum</li><li>Lorem Ipsum</li><li>Lorem Ipsum</li></ul>
  <div class="abs footer-head" style="left:599px">FOLLOW US</div>
  <div class="abs social" role="img" aria-label="Social network links"><i></i><i></i><i></i><i></i></div>
  <div class="abs footer-brand">
    <div class="brand-name">TorvaGrid</div>
    <div class="brand-sub">Systems</div>
  </div>
  <div class="abs copyright">2013 TorvaLink Internet Marketing Service. All rights reserved</div>
</footer>

</body>
</html>
```